Brindle Structures Construction Company Seeking Modern Website

We are a small construction company wanting to create a web presence. We don't have much in the way of current content but will get photos as they come in. Attached is a picture of our business card.
The pages we would like on the menu are:
Home
Portfolio
Product Specs
Testimonials
Our Process
Contact
Some designs we like are:
http://www.tovenquarnsheds.example/
http://www.qzrsheds.example/
http://pannowsheds.example/
http://wistenhalls.example/
Not much requirements other than that so feel free to be creative!
Updates
Target Market(s)
Construction
Commercial and Residential Buildings
Industry/Entity Type
Construction Company
Number of Pages Required
5+ page
Look and feel

```html
<!DOCTYPE html>
<html lang="en">
<head>
<meta charset="utf-8">
<title>Brindle Structures</title>
<link href="https://fonts.googleapis.com/css2?family=Ubuntu:wght@400;500;700&family=Arimo:wght@400;700&display=swap" rel="stylesheet">
<style>
:root{
  --red:#df3a2c;
  --red-dark:#7a1d17;
  --blue:#34a7ec;
  --sky:#3f7fcf;
  --ink:#333;
  --muted:#777;
  --footer:#5a5a5a;
  --footer-text:#e8e8e8;
  --white:#fff;
}
*{margin:0;padding:0;box-sizing:border-box}
html,body{width:1083px;height:1200px;overflow:hidden;background:var(--white)}
body{position:relative;font-family:"Arimo",Arial,sans-serif;color:var(--ink)}
.hero{position:absolute;left:0;top:0;width:1083px;height:522px;overflow:hidden}
.hero-photo{position:absolute;inset:0;background:linear-gradient(180deg,#2f6cc4 0%,#5b95dd 55%,#b9a074 85%,#8c6a42 100%)}
.hero-shape{position:absolute;inset:0}
.contact-top{position:absolute;left:90px;top:26px;color:var(--white)}
.contact-top .row{display:flex;align-items:flex-start;gap:10px}
.contact-top .phone{font-weight:700;font-size:18px;letter-spacing:.5px;line-height:22px}
.contact-top .addr{font-size:14.5px;line-height:20px;margin-top:6px}
.brand{position:absolute;left:88px;top:148px;font-family:"Ubuntu",sans-serif;font-weight:700;font-size:35px;color:var(--blue)}
.headline{position:absolute;left:89px;top:238px;font-family:"Ubuntu",sans-serif;font-weight:500;font-size:32px;line-height:45px;color:var(--white)}
.headline span{color:var(--blue)}
.btn-more{position:absolute;left:90px;top:343px;width:98px;height:41px;border:2px solid var(--white);border-radius:6px;color:var(--white);font-family:"Ubuntu",sans-serif;font-size:16px;display:flex;align-items:center;justify-content:center}
.nav{position:absolute;top:14px;left:498px;display:flex;font-size:13.5px;color:var(--white)}
.nav a{color:var(--white);text-decoration:none;height:30px;display:flex;align-items:center;justify-content:center}
.nav .active{background:var(--red);width:72px}
.nav .i1{margin-left:30px;width:64px}
.nav .i2{margin-left:36px;width:60px}
.nav .i3{margin-left:44px;width:56px}
.nav .i4{margin-left:40px;width:72px}
.welcome{position:absolute;top:562px;left:0;width:1083px;text-align:center}
.welcome h1{font-family:"Ubuntu",sans-serif;font-weight:400;font-size:25px;color:#3a3a3a}
.welcome h1 span{color:var(--blue);font-weight:500}
.welcome p{width:770px;margin:13px auto 0;font-size:12px;line-height:20.7px;color:var(--muted)}
.card{position:absolute;top:717px;width:290px;height:202px}
.card-head{height:32px;background:var(--red);color:var(--white);font-size:13.5px;display:flex;align-items:center;justify-content:space-between;padding:0 12px}
.card-head .arrows{display:flex;gap:10px}
.card-photo{height:170px}
.footer{position:absolute;top:975px;left:0;width:1083px;height:225px;background:var(--footer);color:var(--footer-text)}
.footer h3{position:absolute;top:16px;font-size:15.5px;font-weight:700;color:var(--white)}
.sub-form{position:absolute;left:97px;top:54px;width:279px;height:32px;display:flex}
.sub-form .field{flex:1;background:var(--white);display:flex;align-items:center;gap:8px;padding-left:7px;font-size:11.5px;color:#999}
.sub-form .go{width:90px;background:var(--red);color:var(--white);font-size:15px;display:flex;align-items:center;justify-content:center}
.sub-title{position:absolute;left:96px;top:100px;font-size:13.5px;color:var(--white)}
.sub-text{position:absolute;left:97px;top:124px;width:290px;font-size:12px;line-height:18px;color:#ddd}
.links{position:absolute;left:462px;top:56px;list-style:none;font-size:12px;line-height:21.7px;color:var(--white)}
.social{position:absolute;left:647px;top:47px}
.social .item{display:flex;align-items:center;gap:12px;height:44px;font-size:13px;color:var(--white)}
.social .dot{width:29px;height:29px;border-radius:50%;background:var(--blue);border:3px solid #e4e4e4}
.contact-foot{position:absolute;left:841px;top:69px;color:var(--white)}
.contact-foot .phone{font-weight:700;font-size:16.5px;display:flex;align-items:center;gap:7px}
.contact-foot .addr{font-size:12.5px;line-height:20px;margin-top:6px}
.rule{position:absolute;left:90px;top:188px;width:903px;height:1px;background:#777}
.copy{position:absolute;top:197px;width:100%;text-align:center;font-size:12px;color:var(--white)}
</style>
</head>
<body>
<header class="hero">
  <div class="hero-photo" role="img" aria-label="Photo of two builders in hard hats and safety vests studying plans on a site"></div>
  <svg class="hero-shape" viewBox="0 0 1083 522" aria-hidden="true">
    <path d="M0 0H428C505 95 515 285 395 400C295 490 150 522 30 522H0Z" fill="#3aa9ef"/>
    <path d="M0 0H392C468 92 478 280 358 390C258 472 120 514 0 520Z" fill="#e5433a"/>
    <path d="M0 0H352C425 92 428 272 322 376C232 456 112 496 0 506Z" fill="#7e2119"/>
  </svg>
  <div class="contact-top">
    <div class="row">
      <svg width="21" height="21" viewBox="0 0 24 24"><circle cx="12" cy="12" r="10.5" fill="none" stroke="#fff" stroke-width="2"/><path d="M8 6.5l2 2.5-1.2 1.4c.8 1.7 2 2.9 3.6 3.7l1.4-1.2 2.5 2-1.2 1.8c-3.8-.3-7.4-3.9-7.7-7.7z" fill="#fff"/></svg>
      <span class="phone">9950318842</span>
    </div>
    <div class="row" style="margin-top:4px">
      <svg width="21" height="28" viewBox="0 0 21 28"><path d="M10.5 2a7 7 0 0 1 7 7c0 5-7 12-7 12s-7-7-7-12a7 7 0 0 1 7-7z" fill="none" stroke="#fff" stroke-width="2"/><circle cx="10.5" cy="9" r="2.5" fill="#fff"/><ellipse cx="10.5" cy="25" rx="6" ry="1.6" fill="none" stroke="#fff" stroke-width="1.5"/></svg>
      <div class="addr">48 Kestrel Road,<br>Marlow Vale Wa 6090</div>
    </div>
  </div>
  <div class="brand">Brindle Structures</div>
  <h2 class="headline">WE BUILD <span>YOUR</span><br>IMAGINATION</h2>
  <div class="btn-more">Read More</div>
  <nav class="nav">
    <a class="active">Home</a>
    <a class="i1">About Us</a>
    <a class="i2">Services</a>
    <a class="i3">Portfolio</a>
    <a class="i4">Contact Us</a>
  </nav>
</header>

<section class="welcome">
  <h1>WELCOME TO <span>BRINDLE STRUCTURES</span></h1>
  <p>Lorem ipsum dolor sit amet, consectetur adipiscing elit, sed do eiusmod tempor incididunt ut labore et dolore magna aliqua. Ut enim ad minim veniam, quis nostrud exercitation ullamco laboris nisi ut aliquip ex ea commodo consequat. Duis aute irure dolor in reprehenderit in voluptate velit esse cillum dolore eu fugiat nulla pariatur.</p>
</section>

<article class="card" style="left:90px">
  <div class="card-head"><span>ABOUT OUR WORK</span><span class="arrows"><span>&#10094;</span><span>&#10095;</span></span></div>
  <div class="card-photo" role="img" aria-label="Photo of a builder cutting material on a rooftop" style="background:linear-gradient(180deg,#b9c7d4,#8a8f93 60%,#5a5149)"></div>
</article>
<article class="card" style="left:397px">
  <div class="card-head"><span>MISSION STATEMENT</span><span class="arrows"><span>&#10094;</span><span>&#10095;</span></span></div>
  <div class="card-photo" role="img" aria-label="Photo of two engineers reviewing building plans" style="background:linear-gradient(160deg,#e9edf2,#c9d2dc 55%,#8d98a4)"></div>
</article>
<article class="card" style="left:703px">
  <div class="card-head"><span>OUR WORK GALLERY</span><span class="arrows"><span>&#10094;</span><span>&#10095;</span></span></div>
  <div class="card-photo" role="img" aria-label="Photo of a hard hat, laptop, tape measure and rolled blueprints" style="background:linear-gradient(150deg,#f2c63a,#b9c3cc 50%,#dfe6ec)"></div>
</article>

<footer class="footer">
  <h3 style="left:97px">SUBSCRIBE TO OUR NEWSLETTER</h3>
  <div class="sub-form">
    <div class="field">
      <svg width="24" height="16" viewBox="0 0 24 16"><rect x="1" y="1" width="22" height="14" fill="none" stroke="#bbb"/><path d="M1 1l11 8 11-8" fill="none" stroke="#bbb"/></svg>
      Type Your email address
    </div>
    <div class="go">Subscribe</div>
  </div>
  <div class="sub-title">Our Newsletter Signup</div>
  <p class="sub-text">Lorem ipsum dolor sit amet, consectetur adipiscing elit, sed do eiusmod tempor incididunt.</p>

  <h3 style="left:459px">QUICK LINKS</h3>
  <ul class="links"><li>Home</li><li>About Us</li><li>Services</li><li>Portfolio</li><li>Contact Us</li></ul>

  <h3 style="left:647px">FOLLOW US</h3>
  <div class="social">
    <div class="item"><span class="dot"></span>Chatterline</div>
    <div class="item"><span class="dot" style="background:#3b5a9a"></span>Pagecircle</div>
    <div class="item"><span class="dot" style="background:#1f8fc9"></span>Worklink</div>
  </div>

  <h3 style="left:841px">CONTACT</h3>
  <div class="contact-foot">
    <div class="phone"><svg width="12" height="12" viewBox="0 0 24 24"><path d="M5 2l5 6-2.5 3c1.8 3.4 4 5.6 7.5 7.5l3-2.5 6 5-3 3C11 23 1 13 1 5z" fill="#fff"/></svg>9950318842</div>
    <div class="addr">48 Kestrel Road,<br>Marlow Vale Wa 6090</div>
  </div>

  <div class="rule"></div>
  <div class="copy">Copyright &copy; 2013.All right reserved</div>
</footer>
</body>
</html>
```